Flyer Dachdeckerhandwerk
Zielgruppe
Die Steilhang- und Lichtwerk GmbH ist ein renommiertes, inhabergeführtes Familienunternehmen im Dachdeckerhandwerk. Seit über 30 Jahren stehen wir für höchste Qualität, Zuverlässigkeit und fachgerechte Ausführung – von der ersten Beratung bis zur termintreuen Umsetzung auf der Baustelle. Unsere Kunden profitieren von fundiertem Know-how, eingespielten Abläufen und einem starken Team, das langlebige und wirtschaftliche Lösungen realisiert.
Wir bieten eine begrenzte Aktion an und bieten bis 30.06.2026 eine kostenfreie Dachinspektion.
Die Kunden sollen hierfür bei uns anrufen, oder eine Mail mit dem Betreff 'Dachinspektion 2026' senden.
Aufgabenstellung
Unser CI laden wir hoch.
Es soll modern aussehen.

```html
<!DOCTYPE html>
<html lang="de">
<head>
<meta charset="utf-8">
<title>Flyer – Kostenfreie Dachinspektion</title>
<link href="https://fonts.googleapis.com/css2?family=Oswald:wght@400;500;600;700&family=Poppins:wght@400;500;600&display=swap" rel="stylesheet">
<style>
  :root{
    --teal:#1f7a6a;
    --teal-dark:#17685a;
    --accent:#2cc3a0;
    --ribbon:#a7a9a8;
    --paper:#ffffff;
    --soft:#f3f4f4;
    --text:#5a5d5e;
    --stage:#e9ecec;
  }
  *{margin:0;padding:0;box-sizing:border-box}
  html,body{width:1200px;height:1200px;overflow:hidden;background:var(--stage)}
  .flyer{position:absolute;left:180px;top:20px;width:840px;height:1160px;background:var(--paper);overflow:hidden;font-family:'Poppins',sans-serif}
  .head-band{position:absolute;left:0;top:0;width:840px;height:110px;background:var(--teal)}
  .head-title{position:absolute;left:0;top:12px;width:840px;text-align:center;color:#fff;font-family:'Oswald',sans-serif;font-weight:600;font-size:60px;letter-spacing:-0.5px;line-height:1}
  .hero{position:absolute;left:0;top:110px;width:840px;height:372px;background:linear-gradient(90deg,#1b4d40 0%,#2d5a4a 35%,#6b7d76 65%,#9aa6a4 100%)}
  .hero::after{content:"";position:absolute;inset:0;background:linear-gradient(180deg,rgba(200,180,150,.35) 0%,rgba(0,0,0,0) 30%,rgba(0,0,0,.25) 100%)}
  .ribbon{position:absolute;left:158px;top:92px;width:520px;height:55px}
  .ribbon-text{position:absolute;left:158px;top:98px;width:520px;text-align:center;color:#fff;font-family:'Oswald',sans-serif;font-weight:500;font-size:28px;line-height:40px}
  .ribbon-text::before,.ribbon-text::after{content:"";display:inline-block;width:52px;height:2px;background:#fff;vertical-align:middle;margin:0 18px}
  .hero-copy{position:absolute;left:32px;top:184px;font-family:'Oswald',sans-serif;color:#fff;line-height:1}
  .hero-copy .small{font-size:38px;font-weight:600;line-height:46px}
  .hero-copy .big{font-size:58px;font-weight:700;line-height:62px}
  .hero-copy .accent{color:var(--accent)}
  .hero-rule{position:absolute;left:32px;top:418px;width:152px;height:6px;background:var(--accent)}
  .hero-tag{position:absolute;left:32px;top:436px;color:#fff;font-family:'Oswald',sans-serif;font-weight:500;font-size:17px;line-height:24px}
  .company{position:absolute;left:24px;top:500px;width:400px}
  .company-name{display:flex;align-items:center;gap:14px;color:var(--teal);font-family:'Oswald',sans-serif;font-weight:500;font-size:26px;line-height:30px}
  .company-name .mark{width:26px;height:26px;background:var(--teal);flex:none}
  .company-text{margin-top:18px;color:var(--text);font-size:15.4px;line-height:21.5px}
  .divider{position:absolute;left:428px;top:502px;width:2px;height:268px;background:var(--teal)}
  .feature{position:absolute;display:flex;align-items:center;gap:12px;color:var(--teal);font-family:'Oswald',sans-serif;font-weight:500;font-size:19px;line-height:26px}
  .feature svg{width:62px;height:62px;flex:none}
  .values-text{position:absolute;left:446px;top:660px;width:380px;color:var(--text);font-size:15.4px;line-height:21.5px}
  .promo{position:absolute;left:16px;top:781px;width:804px;height:207px;background:var(--teal);border-radius:20px}
  .promo-frame{position:absolute;left:16px;top:12px;width:772px;height:183px;border:2px dashed rgba(255,255,255,.85);border-radius:14px}
  .promo-icon{position:absolute;left:62px;top:28px;width:140px;height:120px}
  .promo-date{position:absolute;left:250px;top:34px;width:360px;text-align:center;color:#fff;font-family:'Oswald',sans-serif;font-weight:500;font-size:25px}
  .promo-date::before,.promo-date::after{content:"";display:inline-block;width:30px;height:2px;background:#fff;vertical-align:middle;margin:0 10px}
  .promo-title{position:absolute;left:256px;top:70px;color:#fff;font-family:'Oswald',sans-serif;font-weight:600;font-size:42px;line-height:44px;letter-spacing:-0.3px}
  .promo-note{position:absolute;left:0;top:170px;width:804px;text-align:center;color:#fff;font-size:16.5px}
  .seal{position:absolute;left:632px;top:32px;width:116px;height:116px}
  .contact{position:absolute;left:24px;top:1003px;width:800px;height:123px;background:var(--soft)}
  .contact-sep{position:absolute;left:400px;top:22px;width:2px;height:80px;background:#dfe1e1}
  .contact-item{position:absolute;top:20px;display:flex;align-items:center;gap:16px}
  .contact-item svg{width:76px;height:76px;flex:none}
  .contact-call{font-family:'Oswald',sans-serif;font-weight:500;color:var(--teal);font-size:37px;line-height:38px}
  .contact-sub{font-size:11.5px;color:var(--text);line-height:14px}
  .contact-phone{font-family:'Poppins',sans-serif;font-weight:600;color:var(--teal);font-size:30px;line-height:38px;letter-spacing:1px}
  .contact-mail{font-family:'Poppins',sans-serif;font-weight:600;color:var(--teal);font-size:19px;line-height:38px}
  .foot-band{position:absolute;left:0;top:1138px;width:840px;height:22px;background:var(--teal)}
</style>
</head>
<body>
<main class="flyer">
  <div class="head-band"></div>
  <div class="hero" role="img" aria-label="Foto: modernes Flachdach mit Begrünung und Solarmodulen über einer Stadt in der Abenddämmerung"></div>
  <h1 class="head-title">KOSTENFREIE DACHINSPEKTION!</h1>
  <svg class="ribbon" viewBox="0 0 520 55"><polygon points="0,0 520,0 470,55 50,55" fill="var(--ribbon)"/></svg>
  <div class="ribbon-text">NUR FÜR KURZE ZEIT</div>

  <div class="hero-copy">
    <div class="small">SICHERN SIE SICH</div>
    <div class="small">JETZT IHRE</div>
    <div class="big accent">KOSTENLOSE</div>
    <div class="big">DACHPRÜFUNG</div>
  </div>
  <div class="hero-rule"></div>
  <div class="hero-tag">PROFESSIONELL. ZUVERLÄSSIG. UNVERBINDLICH.</div>

  <section class="company">
    <div class="company-name"><span class="mark"></span><span>Steilhang- und<br>Lichtwerk GmbH</span></div>
    <p class="company-text">Die Steilhang- und Lichtwerk GmbH ist ein renommiertes, inhabergeführtes Familienunternehmen im Dachdeckerhandwerk.<br>Seit über 30 Jahren stehen wir für höchste Qualität, Zuverlässigkeit und fachgerechte Ausführung von der ersten Beratung bis zur termingerechten Umsetzung auf der Baustelle.</p>
  </section>
  <div class="divider"></div>

  <div class="feature" style="left:446px;top:505px">
    <svg viewBox="0 0 62 62"><circle cx="31" cy="31" r="28" fill="none" stroke="var(--teal)" stroke-width="3"/><path d="M31 14 L44 19 V30 C44 39 38 45 31 48 C24 45 18 39 18 30 V19 Z" fill="var(--teal)"/><path d="M25 31 L30 36 L38 26" fill="none" stroke="#fff" stroke-width="3.5" stroke-linecap="round" stroke-linejoin="round"/></svg>
    <span>HÖCHSTE<br>QUALITÄT</span>
  </div>
  <div class="feature" style="left:616px;top:530px">
    <svg viewBox="0 0 62 62"><circle cx="31" cy="31" r="28" fill="none" stroke="var(--teal)" stroke-width="3"/><path d="M17 34 C17 24 23 18 31 18 C39 18 45 24 45 34 Z" fill="var(--teal)"/><rect x="14" y="34" width="34" height="5" rx="2" fill="var(--teal)"/><rect x="29" y="15" width="4" height="12" fill="#fff"/><rect x="20" y="42" width="22" height="6" rx="2" fill="var(--teal)"/></svg>
    <span>FACHGERECHTE<br>AUSFÜHRUNG</span>
  </div>
  <div class="feature" style="left:446px;top:575px">
    <svg viewBox="0 0 62 62"><circle cx="31" cy="31" r="28" fill="none" stroke="var(--teal)" stroke-width="3"/><path d="M12 28 L22 22 L31 27 L40 22 L50 28 L44 38 L36 44 L26 40 L18 36 Z" fill="var(--teal)"/><path d="M24 33 L31 38 M28 30 L35 35" stroke="#fff" stroke-width="2.5" stroke-linecap="round"/></svg>
    <span>ZUVERLÄSSIG<br>UND FAIR</span>
  </div>
  <p class="values-text">Unsere Kunden profitieren von fundiertem Know-how, eingespielten Abläufen und einem starken Team, das langlebige und wirtschaftliche Lösungen realisiert.</p>

  <section class="promo">
    <div class="promo-frame"></div>
    <svg class="promo-icon" viewBox="0 0 140 120"><circle cx="58" cy="54" r="46" fill="none" stroke="#fff" stroke-width="8"/><line x1="92" y1="88" x2="128" y2="116" stroke="#fff" stroke-width="12" stroke-linecap="round"/><path d="M30 56 L58 30 L86 56 L80 56 L80 80 L36 80 L36 56 Z" fill="#fff"/><rect x="72" y="30" width="7" height="14" fill="#fff"/><rect x="51" y="62" width="14" height="18" fill="var(--teal)"/></svg>
    <div class="promo-date">AKTION BIS 30.06.2026</div>
    <div class="promo-title">100% KOSTENFREIE<br>DACHINSPEKTION</div>
    <div class="promo-note">Lassen Sie Ihr Dach professionell prüfen schnell, zuverlässig und unverbindlich!</div>
    <svg class="seal" viewBox="0 0 116 116"><circle cx="58" cy="58" r="56" fill="var(--accent)"/><circle cx="58" cy="58" r="48" fill="none" stroke="#fff" stroke-width="1.5" stroke-dasharray="5 4"/><g transform="rotate(8 58 58)" fill="#fff" font-family="Oswald, sans-serif" font-weight="600" font-size="17" text-anchor="middle"><text x="58" y="42">IHR DACH</text><text x="58" y="61">IN BESTEN</text><text x="58" y="80">HÄNDEN!</text></g><path d="M50 92 L56 97 L66 88" fill="none" stroke="#fff" stroke-width="2" stroke-linecap="round"/></svg>
  </section>

  <section class="contact">
    <div class="contact-item" style="left:26px">
      <svg viewBox="0 0 76 76"><circle cx="38" cy="38" r="38" fill="var(--teal)"/><path d="M26 20 C23 20 20 23 21 28 C24 42 34 52 48 55 C53 56 56 53 56 50 L56 46 L47 42 L42 47 C36 44 32 40 29 34 L34 29 L30 20 Z" fill="#fff"/></svg>
      <div><div class="contact-call">JETZT ANRUFEN</div><div class="contact-sub">UND TERMIN SICHERN!</div><div class="contact-phone">06221-4473-0</div></div>
    </div>
    <div class="contact-sep"></div>
    <div class="contact-item" style="left:438px">
      <svg viewBox="0 0 76 76"><circle cx="38" cy="38" r="38" fill="var(--teal)"/><rect x="20" y="26" width="36" height="25" rx="3" fill="none" stroke="#fff" stroke-width="3.5"/><path d="M21 28 L38 41 L55 28" fill="none" stroke="#fff" stroke-width="3.5" stroke-linejoin="round"/></svg>
      <div><div class="contact-call">JETZT SCHREIBEN</div><div class="contact-sub">BETREFF: „DACHINSPEKTION 2026“</div><div class="contact-mail">info@steilhang-licht.de</div></div>
    </div>
  </section>
  <div class="foot-band"></div>
</main>
</body>
</html>
```